Splash Page Design For Thailands "Whatever Suits Me" App

We are creating an app that will allow a tourist to request a variety of services on demand. Such as motorbike rentals, in room massage, pick up and laundry delivery service, maid cleaning service, etc.

We want to design a splash page that tourists will initially go to when they want to choose a service that we offer.

INSTRUCTIONS:
This page must speak to tourists in Phuket, Thailand. Should be Thailand Island theme.

GO 4 IT (logo)

CONTENT:

ALL YOU NEED WHILE TRAVELING IN PHUKET, THAILAND

CHOOSE A SERVICE BELOW TO GET STARTED

MOTORBIKE RENTALS
ACTIVITY AND TOUR PACKAGES (COMING SOON)
LAUNDRY PICK UP AND DELIVER SERVICE (COMING SOON)
MAID SERVICE (COMING SOON)
MASSAGE SERVICE TO YOUR ROOM (COMING SOON)
VISA SERVICE (COMING SOON)

Target Market(s)

TOURISTS IN PHUKET THAILAND

Industry/Entity Type

TOURISM

Number of Pages Required

1 page

Requirements
Must have
• We are creating an app that will allow a tourist to request a variety of services on demand. Such as motorbike rentals, in room massage, pick up and laundry delivery service, maid cleaning service, etc. We want to design a splash page that tourists will initially go to when they want to choose a service that we offer. INSTRUCTIONS: This page must speak to tourists in Phuket, Thailand. Should be Thailand Island theme. GO 4 IT (logo) CONTENT: ALL YOU NEED WHILE TRAVELING IN PHUKET, THAILAND CHOOSE A SERVICE BELOW TO GET STARTED MOTORBIKE RENTALS ACTIVITY AND TOUR PACKAGES (COMING SOON) LAUNDRY PICK UP AND DELIVER SERVICE (COMING SOON) MAID SERVICE (COMING SOON) MASSAGE SERVICE TO YOUR ROOM (COMING SOON) VISA SERVICE (COMING SOON)
Nice to have
Should not have

```html
<!DOCTYPE html>
<html lang="en">
<head>
<meta charset="utf-8">
<title>GO 4 IT — Whatever Suits Me</title>
<link href="https://fonts.googleapis.com/css2?family=Bebas+Neue&display=swap" rel="stylesheet">
<style>
  :root {
    --backdrop: #245437;
    --orange: #f7941d;
    --white: #ffffff;
    --ink: #1a1a1a;
    --sky: #8c9294;
    --band: rgba(200, 202, 204, 0.55);
    --ring: rgba(255, 255, 255, 0.16);
  }
  * { margin: 0; padding: 0; box-sizing: border-box; }
  html, body {
    width: 1200px; height: 1200px; overflow: hidden;
    background: var(--backdrop);
    font-family: "Bebas Neue", "Oswald", sans-serif;
  }
  .screen {
    position: absolute; left: 344px; top: 30px;
    width: 512px; height: 1140px;
    overflow: hidden;
  }
  .island-photo {
    position: absolute; inset: 0;
    background:
      linear-gradient(180deg,
        #8f9597 0%, #8a9193 11%, #7f8c7d 18%,
        #4f7a2a 26%, #3f6d22 40%, #557a35 55%,
        #7d7f78 64%, #6a6f66 72%, #4b5246 78%,
        #2f7c86 82%, #2b8a95 90%, #3a93a0 100%);
  }
  .decor { position: absolute; inset: 0; }
  .top-bar {
    position: absolute; left: 0; top: 0; width: 100%; height: 132px;
  }
  .menu-btn {
    position: absolute; left: 67px; top: 58px; width: 48px; height: 36px;
  }
  .menu-btn span {
    position: absolute; left: 0; height: 5px; border-radius: 3px; background: var(--white);
  }
  .menu-btn span:nth-child(1) { top: 0; width: 47px; }
  .menu-btn span:nth-child(2) { top: 15px; width: 47px; }
  .menu-btn span:nth-child(3) { top: 30px; width: 33px; }
  .search-btn { position: absolute; left: 416px; top: 55px; width: 36px; height: 36px; }
  .brand-band {
    position: absolute; left: 0; top: 132px; width: 100%; height: 70px;
    background: var(--band);
    display: flex; align-items: center; justify-content: center;
  }
  .brand-name {
    color: var(--orange); font-size: 30px; letter-spacing: 2px; line-height: 1;
  }
  .headline {
    position: absolute; left: 49px; top: 238px;
    color: var(--white); font-weight: 400;
    font-size: 70px; line-height: 77px; letter-spacing: 0.5px;
  }
  .headline .accent {
    display: block; color: var(--orange);
    font-size: 110px; line-height: 112px; margin-top: -2px;
  }
  .prompt {
    position: absolute; left: 0; width: 100%; top: 618px;
    text-align: center; color: var(--white);
    font-size: 27px; line-height: 30px; padding-left: 6px;
  }
  .services { position: absolute; left: 45px; top: 679px; width: 415px; list-style: none; }
  .service {
    position: relative; height: 58px; margin-bottom: 25px;
    background: var(--orange); border-radius: 29px;
    display: flex; align-items: center;
  }
  .service svg { position: absolute; left: 30px; top: 9px; width: 42px; height: 40px; }
  .service-label {
    margin-left: 94px; color: var(--white);
    font-size: 19px; line-height: 21px; letter-spacing: 0.2px;
  }
</style>
</head>
<body>
<main class="screen">
  <div class="island-photo" role="img" aria-label="Photo of a green limestone island rising from turquoise sea under a grey sky, Phuket"></div>

  <svg class="decor" width="512" height="1140" viewBox="0 0 512 1140" aria-hidden="true">
    <circle cx="38" cy="18" r="124" fill="rgba(90,96,98,0.35)"/>
    <circle cx="38" cy="18" r="143" fill="none" stroke="var(--ring)" stroke-width="38"/>
    <circle cx="410" cy="536" r="235" fill="none" stroke="var(--ring)" stroke-width="42"/>
    <circle cx="166" cy="1135" r="125" fill="none" stroke="var(--ring)" stroke-width="42"/>
  </svg>

  <header class="top-bar">
    <div class="menu-btn" aria-label="Menu"><span></span><span></span><span></span></div>
    <svg class="search-btn" viewBox="0 0 36 36" aria-label="Search">
      <circle cx="13" cy="13" r="9.5" fill="none" stroke="#fff" stroke-width="4"/>
      <line x1="20" y1="20" x2="32" y2="32" stroke="#fff" stroke-width="5" stroke-linecap="round"/>
    </svg>
  </header>

  <div class="brand-band">
    <span class="brand-name">GO 4 IT</span>
  </div>

  <h1 class="headline">
    All you need<br>while traveling<br>in Phuket,
    <span class="accent">Thailand</span>
  </h1>

  <p class="prompt">Choose a service below to get started</p>

  <ul class="services">
    <li class="service">
      <svg viewBox="0 0 42 40" fill="none" stroke="#1a1a1a" stroke-width="1.6" aria-hidden="true">
        <path d="M9 36 C3 28 2 25 2 22 a7 7 0 0 1 14 0 c0 3 -1 6 -7 14z"/><circle cx="9" cy="22" r="2.6"/>
        <path d="M33 20 c-4 -6 -5 -8 -5 -10 a5 5 0 0 1 10 0 c0 2 -1 4 -5 10z"/><circle cx="33" cy="10" r="1.8"/>
        <path d="M12 36 H40 V28 H20" stroke-dasharray="2 2"/>
      </svg>
      <span class="service-label">Motorbike rentals activity and tour packages<br>(coming soon)</span>
    </li>
    <li class="service">
      <svg viewBox="0 0 42 40" fill="none" stroke="#1a1a1a" stroke-width="1.6" aria-hidden="true">
        <rect x="12" y="3" width="26" height="34" rx="2"/><line x1="12" y1="10" x2="38" y2="10"/>
        <circle cx="25" cy="23" r="8"/><path d="M19 23 c3 -3 6 3 12 0"/>
        <rect x="2" y="28" width="9" height="3"/><rect x="2" y="32" width="9" height="3"/>
      </svg>
      <span class="service-label">Laundry pick up and deliver service<br>(coming soon)</span>
    </li>
    <li class="service">
      <svg viewBox="0 0 42 40" fill="none" stroke="#1a1a1a" stroke-width="1.6" aria-hidden="true">
        <line x1="12" y1="2" x2="12" y2="30"/><path d="M5 36 c0 -5 3 -7 7 -7 s7 2 7 7z"/>
        <path d="M22 18 H40 L37 38 H25z"/><path d="M24 18 c0 -8 14 -8 14 0"/>
      </svg>
      <span class="service-label">Maid service (coming soon)</span>
    </li>
    <li class="service">
      <svg viewBox="0 0 42 40" fill="none" stroke="#1a1a1a" stroke-width="1.6" aria-hidden="true">
        <rect x="3" y="24" width="36" height="5" rx="2"/>
        <line x1="8" y1="29" x2="8" y2="38"/><line x1="34" y1="29" x2="34" y2="38"/>
        <rect x="14" y="18" width="18" height="6" rx="3"/>
      </svg>
      <span class="service-label">Massage service to your room (coming soon)</span>
    </li>
    <li class="service">
      <svg viewBox="0 0 42 40" fill="none" stroke="#1a1a1a" stroke-width="2" aria-hidden="true">
        <rect x="2" y="6" width="38" height="28" rx="3"/>
        <line x1="2" y1="14" x2="40" y2="14" stroke-width="4"/>
        <line x1="7" y1="26" x2="20" y2="26"/>
      </svg>
      <span class="service-label">Visa service (coming soon)</span>
    </li>
  </ul>
</main>
</body>
</html>
```